FR banner

we need a banner design (36"x120" horizontal) that will be displayed on a local high school baseball field. My company ( Crestwell Prints Co) has been producing signage for the Fernmoor Ridge community since 2009. We would like to communicate that we do more than banners. The final design should include the slogan "Signs Shirts Swag" and our Logo.

Target Market(s)

companies, teams, events, shirt and other marketing items.

Industry/Entity Type

Sign, Print,

Font styles to use
Sans Serif

Requirements
Should not have
• no baseball content.

```html
<!DOCTYPE html>
<html lang="en">
<head>
<meta charset="utf-8">
<title>Crestwell Prints Co – Field Banner</title>
<link rel="stylesheet" href="https://fonts.googleapis.com/css2?family=Rye&family=Montserrat:wght@800;900&display=swap">
<style>
  :root {
    --page-bg: #e9e9e9;
    --banner-black: #000000;
    --frame-white: #ffffff;
    --brand-blue: #18b9ec;
    --mark-white: #e4e4e4;
  }
  html, body {
    margin: 0;
    padding: 0;
    width: 1200px;
    height: 1000px;
    overflow: hidden;
    background: var(--page-bg);
  }
  .canvas {
    position: relative;
    width: 1200px;
    height: 1000px;
  }
  .banner {
    position: absolute;
    left: 0;
    top: 0;
  }
  .slogan-western {
    font-family: "Rye", serif;
    font-size: 92px;
    fill: var(--brand-blue);
  }
  .slogan-swag {
    font-family: "Montserrat", sans-serif;
    font-weight: 900;
    font-size: 92px;
    fill: var(--brand-blue);
  }
  .company-name {
    font-family: "Montserrat", sans-serif;
    font-weight: 800;
    font-size: 27px;
    fill: var(--mark-white);
  }
  .ornament-area {
    position: absolute;
    left: 556px;
    top: 600px;
    width: 88px;
    height: 32px;
    background: var(--frame-white);
    border-radius: 6px;
  }
</style>
</head>
<body>
<main class="canvas">
  <svg class="banner" width="1200" height="1000" viewBox="0 0 1200 1000" aria-label="Crestwell Prints Co banner: Signs, Shirts, Swag">
    <rect class="banner-field" x="30" y="330" width="1140" height="340" fill="var(--banner-black)"/>
    <polygon class="banner-frame" points="42,392 600,342 1158,392 1158,548 600,657 42,548"
             fill="none" stroke="var(--frame-white)" stroke-width="4"/>

    <rect class="side-diamond" x="74" y="457" width="12" height="12" transform="rotate(45 80 463)" fill="var(--frame-white)"/>
    <rect class="side-diamond" x="1114" y="457" width="12" height="12" transform="rotate(45 1120 463)" fill="var(--frame-white)"/>

    <text class="slogan-western" x="112" y="490" textLength="393" lengthAdjust="spacingAndGlyphs">SIGNS</text>
    <text class="slogan-western" x="692" y="490" textLength="398" lengthAdjust="spacingAndGlyphs">SHIRTS</text>

    <text class="company-name" x="600" y="440" text-anchor="middle" textLength="160" lengthAdjust="spacingAndGlyphs">Crestwell</text>
    <text class="company-name" x="600" y="476" text-anchor="middle" textLength="160" lengthAdjust="spacingAndGlyphs">Prints Co</text>

    <line class="divider" x1="100" y1="537" x2="370" y2="537" stroke="var(--frame-white)" stroke-width="2"/>
    <line class="divider" x1="830" y1="537" x2="1100" y2="537" stroke="var(--frame-white)" stroke-width="2"/>

    <text class="slogan-swag" x="600" y="585" text-anchor="middle" textLength="400" lengthAdjust="spacingAndGlyphs">SWAG</text>
  </svg>
  <div class="ornament-area" role="img" aria-label="Small white decorative scroll flourish"></div>
</main>
</body>
</html>
```